Packaged Food Business Needs a Packaging Design

We need a package design to be used as a label/sticker on the lids of round and square transparent plastic containers and on the sides of resealable stand-up pouches. The brand name is 'Savourly' - please find attached logo together with pictures of the sample containers and pouch. We will use the packaging to market a wide variety of food categories from nuts, dried fruits, spices, cooking chocolates, baking ingredients, cereals, grains and pulses.

OVERALL FEEDBACK ON DESIGNS ALREADY RECEIVED:

- We have found so far that a lot of our mandatory requirements are not adhered to in designs that have been submitted so far. We would like to emphasise that the ingredient, weight and expiry text will be printed at the time of packing so it should not take prime space on the pack BUT at the same time some 'blank' space needs to flawlessly be incorporated into the overall design for this purpose
- We encourage you to glorify the brand logo in the pack, and absolutely refrain from duplicating the tagline
- Please note that ONE label design will be used to pack a wide variety of food ingredients and therefore please ensure that the choice of your design incorporates this requirement, in the past we have received designs that are limited to only one type of food (like nuts) or have received designs that are too floral or leafy (and not grounded to food
- Please ensure that you submit designs for all three packaging formats, it is critical to see the family look from the on-set

Target Market(s)

The brand is targeting both mothers and professional chefs and therefore the label design should be broadly approachable and convey affordable premium

Industry/Entity Type

Business

Requirements
Must have
• - Consistent with the brand name and logo, the overall look and feel of the packaging should convey values of healthy, gourmet food ingredients, high in nourishment and project a sense of delightful taste
• - The design styling to be modern and 'simplistic' (embracing 'less-is-more' type of a design style)
• - Design a packaging architecture that incorporates the brand logo together with its tagline lock-up of 'taste the goodness in every spoonful' - find logo attached
• - The design needs to have a dedicated area to print the ingredient (e.g., Mixed Nuts), weight (e.g., 500g) and expiry (this space needs to be flawlessly incorporated into the design) - this information will be printed either with an inkjet printer or with a rubber stamp so please leave an empty space (the text should not be part of the design, just the area for the text needs to be included in the design)
• - The packaging must include 'Packed By: Mwenda Traders Ltd, P. O. Box 41562, Kampala - Uganda'
• - For the design of the resealable pouch, please incorporate a window to see through the ingredients and a hole on top to hang on supermarket pegs if necessary
Nice to have
• - We would love to have some design submissions that are bold and cheerful and fun (but not frivolous) - please see attached inspiration for 'fun' packaging. The attachments are purely for inspiration, not to infringe on anyone else's TM and copyrights
• - Incorporate green to convey healthy, organic values
• - Explore use of gold and silver convey premiumness
Should not have
• - Do not duplicate the tagline
• - Do not include the ingredient, weight and expiry in the main graphic of the design, these will be printed at the time of packing so ensure there is provision for this in a flawless way in the design (e.g., via a blank space allocated for this purpose)

```html
<!DOCTYPE html>
<html lang="en">
<head>
<meta charset="utf-8">
<title>Savourly – Round Lid Label</title>
<link rel="stylesheet" href="https://fonts.googleapis.com/css2?family=Bebas+Neue&family=Montserrat:wght@700;800&family=Myriad+Pro&family=Source+Sans+3:wght@400;700&display=swap">
<style>
  :root {
    --paper: #ffffff;
    --outline: #1a1a1a;
    --brand-brown: #44230a;
    --tagline-green: #4a8a1e;
    --band-olive: #b09a22;
    --band-rose: #b46a55;
    --band-lime: #9cc83c;
    --band-ochre: #a67c28;
    --ink: #111111;
  }
  html, body {
    margin: 0;
    padding: 0;
    width: 1200px;
    height: 1200px;
    overflow: hidden;
    background: var(--paper);
  }
  .lid-label {
    display: block;
    width: 1200px;
    height: 1200px;
  }
  .label-face { fill: var(--paper); stroke: var(--outline); stroke-width: 1; }
  .brand-wordmark {
    font-family: "Bebas Neue", "Oswald", sans-serif;
    font-size: 94px;
    fill: var(--brand-brown);
  }
  .brand-tagline {
    font-family: "Montserrat", sans-serif;
    font-weight: 800;
    font-size: 14px;
    fill: var(--tagline-green);
  }
  .packer-line, .ingredients-line {
    font-family: "Source Sans 3", sans-serif;
    font-size: 10px;
    fill: var(--ink);
  }
  .ingredients-label { font-weight: 700; }
</style>
</head>
<body>
<svg class="lid-label" viewBox="0 0 1200 1200" xmlns="http://www.w3.org/2000/svg">
  <defs>
    <clipPath id="lid-shape">
      <circle cx="618" cy="603" r="306"/>
    </clipPath>
    <linearGradient id="band-tones" x1="0" y1="0" x2="1" y2="0">
      <stop offset="0" stop-color="var(--band-rose)"/>
      <stop offset="0.22" stop-color="var(--band-olive)"/>
      <stop offset="0.45" stop-color="var(--band-lime)"/>
      <stop offset="0.62" stop-color="var(--band-ochre)"/>
      <stop offset="0.8" stop-color="var(--band-olive)"/>
      <stop offset="1" stop-color="var(--band-rose)"/>
    </linearGradient>
  </defs>

  <circle class="label-face" cx="618" cy="603" r="306"/>

  <g class="brand-lockup">
    <text class="brand-wordmark" x="422" y="510" textLength="410" lengthAdjust="spacing">SAVOURLY</text>
    <text class="brand-tagline" x="422" y="533" textLength="400" lengthAdjust="spacing">TASTE THE GOODNESS IN EVERY SPOONFUL!</text>
  </g>

  <g class="decor-band" clip-path="url(#lid-shape)">
    <rect x="300" y="560" width="640" height="212" fill="url(#band-tones)" role="img" aria-label="Band of textured circles in olive, rose, lime and brown with line-drawn wheat ears"/>
  </g>

  <g class="pack-info">
    <text class="packer-line" x="474" y="804">Packed By: Mwenda Traders Ltd, P. O. Box 41562, Kampala - Uganda</text>
    <text class="ingredients-line" x="474" y="818"><tspan class="ingredients-label">Ingredients:</tspan> ...</text>
  </g>
</svg>
</body>
</html>
```